Brintell's Business Card

I need some designs for a new business card including the new logo attached. An old example of our business card is also attached to show all the data that should be included on the new design.
**I added some more examples someone had mocked up**

Contact Information for Business Card

Should include all info on other examples uploaded.

```html
<!DOCTYPE html>
<html lang="en">
<head>
<meta charset="utf-8">
<title>Brintell's Business Card</title>
<link rel="stylesheet" href="https://fonts.googleapis.com/css2?family=Source+Sans+3:wght@400;700&display=swap">
<style>
  :root {
    --page-bg: #e4e4e4;
    --card-dark: #231f20;
    --card-light: #f3f3f3;
    --brand-blue: #0f6db3;
    --brand-red: #e21f26;
    --ink: #333333;
    --white: #ffffff;
  }
  html, body {
    margin: 0;
    padding: 0;
    width: 1200px;
    height: 960px;
    overflow: hidden;
    background: var(--page-bg);
    font-family: "Source Sans 3", "Source Sans Pro", Arial, sans-serif;
  }
  .card {
    position: absolute;
    left: 297px;
    width: 609px;
    height: 348px;
    overflow: hidden;
  }
  .card-front { top: 109px; background: var(--card-dark); }
  .card-back { top: 511px; background: var(--card-light); }
  .card svg.shapes { position: absolute; left: 0; top: 0; }

  .service-area {
    position: absolute; top: 28px; left: 0; width: 100%;
    text-align: center; color: var(--brand-blue);
    font-weight: 700; font-size: 20px; letter-spacing: 0.8px;
  }
  .service-area .dot { color: var(--brand-red); }

  .brand-name {
    position: absolute; display: flex; align-items: center; gap: 12px;
    color: var(--brand-blue); font-weight: 700; line-height: 1;
  }
  .brand-mark { border-radius: 50%; background: var(--brand-red); flex: none; }
  .card-front .brand-name { left: 0; width: 100%; justify-content: center; top: 142px; font-size: 50px; }
  .card-front .brand-mark { width: 26px; height: 26px; }
  .card-back .brand-name { left: 52px; top: 66px; font-size: 50px; }
  .card-back .brand-mark { width: 26px; height: 26px; }

  .call-today {
    position: absolute; left: 213px; top: 263px; width: 183px; height: 35px;
    border-radius: 18px; background: var(--brand-red); color: var(--white);
    font-weight: 700; font-size: 20px; text-align: center; line-height: 35px;
  }
  .needs {
    position: absolute; left: 0; width: 100%; top: 308px;
    text-align: center; color: var(--white); font-weight: 700;
    font-size: 18px; letter-spacing: 0.5px;
  }

  .person { position: absolute; left: 52px; top: 198px; }
  .person-name { color: var(--brand-blue); font-weight: 700; font-size: 25px; line-height: 1.1; }
  .person-role { color: var(--brand-red); font-size: 15px; margin-top: 2px; }
  .contact { position: absolute; left: 52px; top: 269px; color: var(--ink); font-size: 16px; }
  .contact-line { display: flex; align-items: center; gap: 7px; height: 21px; }
  .contact-line svg { flex: none; }

  .badge {
    position: absolute; color: var(--white); font-weight: 700; font-size: 16px;
    line-height: 42px; text-align: center;
  }
  .badge-licensed { left: 386px; top: 221px; width: 210px; }
  .badge-family { left: 345px; top: 276px; width: 240px; line-height: 43px; }
</style>
</head>
<body>

<section class="card card-front">
  <svg class="shapes" width="609" height="348" viewBox="0 0 609 348">
    <path d="M0 294 Q304 258 609 294 L609 348 L0 348 Z" fill="var(--brand-red)"/>
    <path d="M0 300 Q304 268 609 300 L609 348 L0 348 Z" fill="var(--brand-blue)"/>
  </svg>
  <p class="service-area" style="margin:0">SERVES FAIRHAVEN <span class="dot">•</span> IA &amp; SURROUNDING AREAS</p>
  <div class="brand-name"><span class="brand-mark"></span>BRINTELL'S</div>
  <div class="call-today">CALL TODAY</div>
  <p class="needs" style="margin:0">FOR ALL YOUR HVAC, REFRIGERATION &amp; PLUMBING NEEDS</p>
</section>

<section class="card card-back">
  <svg class="shapes" width="609" height="348" viewBox="0 0 609 348">
    <path d="M505 0 L609 0 L609 348 L418 348 Q468 300 470 200 Q471 110 466 70 Q466 0 505 0 Z" fill="var(--card-dark)"/>
    <polygon points="386,221 609,221 609,263 365,263" fill="var(--brand-blue)"/>
    <polygon points="333,276 609,276 609,319 311,319" fill="var(--brand-red)"/>
  </svg>
  <div class="brand-name"><span class="brand-mark"></span>BRINTELL'S</div>

  <div class="person">
    <div class="person-name">Dale Brintell</div>
    <div class="person-role">Co-Owner</div>
  </div>

  <div class="contact">
    <div class="contact-line">
      <svg width="14" height="14" viewBox="0 0 24 24"><path d="M6.6 10.8a15.1 15.1 0 0 0 6.6 6.6l2.2-2.2a1 1 0 0 1 1-.25 11.4 11.4 0 0 0 3.6.57 1 1 0 0 1 1 1V20a1 1 0 0 1-1 1A17 17 0 0 1 3 4a1 1 0 0 1 1-1h3.5a1 1 0 0 1 1 1c0 1.25.2 2.45.57 3.6a1 1 0 0 1-.25 1z" fill="var(--brand-red)"/></svg>
      <span>555.014.2287</span>
    </div>
    <div class="contact-line">
      <svg width="14" height="12" viewBox="0 0 24 18"><rect x="1.5" y="1.5" width="21" height="15" rx="1.5" fill="none" stroke="var(--brand-red)" stroke-width="3"/><path d="M2 2 L12 10 L22 2" fill="none" stroke="var(--brand-red)" stroke-width="3"/></svg>
      <span>brintellhvac@mailbox.com</span>
    </div>
  </div>

  <div class="badge badge-licensed">LICENSED &amp; INSURED</div>
  <div class="badge badge-family">FAMILY OWNED &amp; OPERATED</div>
</section>

</body>
</html>
```